"Rise. Shift. Thrive." Empowerment Book Cover

Hello, I need a hot, trendy, and contemporary book cover designed for my first book called "Rise. Shift. Thrive. -- 360 Bold Momentum Notes to Guide Anyone to Rise, Shift, and Thrive in Their Career & Daily Dreams."
This is my first book and I am really wanting to launch my brand with it... it would be awesome to match the inside/outside branding of the book. So we can either create the book cover to match the book guts, or update the book guts to match the cover.
Lastly, I just got a professional photoshoot done last week so we can use one of those images, or we can go with a different idea/style for the cover. The body of the book is attached. All questions welcomed, happy designing!
Target Market(s)
Gen Z, Millennials and Gen X.
Industry/Entity Type
Personal Development.
Requirements
Must have
- It must stand out and be different from other typical book covers.
Nice to have
- Success, Inspiration, Motivation, Mindset, Growth.
Should not have
- Clipart, stock art, stock look and feel.

```html
<!DOCTYPE html>
<html lang="en">
<head>
<meta charset="UTF-8">
<title>Rise. Shift. Thrive. — Book Cover</title>
<link rel="stylesheet" href="https://fonts.googleapis.com/css2?family=Anton&family=Josefin+Sans:wght@700&display=swap">
<style>
  :root {
    --page: #ffffff;
    --brand-blue: #0b4f9c;
    --brand-blue-deep: #134a8a;
    --slate: #3f4b52;
    --cover-top: #e7eff7;
    --cover-bottom: #c9d0d8;
    --initial: #e4e4e4;
  }
  * { margin: 0; padding: 0; box-sizing: border-box; }
  html, body {
    width: 1200px;
    height: 1200px;
    overflow: hidden;
    background: var(--page);
  }
  .book-cover {
    position: absolute;
    left: 227px;
    top: 40px;
    width: 746px;
    height: 1120px;
    background: linear-gradient(170deg, var(--cover-top) 0%, #dde4ec 55%, var(--cover-bottom) 100%);
    overflow: hidden;
  }
  .spine-band {
    position: absolute;
    left: 0;
    top: 0;
    width: 205px;
    height: 100%;
    background: linear-gradient(180deg, var(--brand-blue) 0%, var(--brand-blue-deep) 100%);
  }
  .count {
    position: absolute;
    left: 232px;
    top: 134px;
    font-family: 'Anton', sans-serif;
    font-size: 122px;
    line-height: 1;
    color: var(--slate);
    letter-spacing: 1px;
  }
  .tagline {
    position: absolute;
    left: 235px;
    font-family: 'Josefin Sans', sans-serif;
    font-weight: 700;
    font-size: 29px;
    line-height: 1;
    letter-spacing: 1.5px;
    color: var(--brand-blue);
    white-space: nowrap;
  }
  .tagline--one { top: 278px; }
  .tagline--two { top: 314px; }
  .tagline .accent { color: var(--slate); }
  .title-row {
    position: absolute;
    left: 0;
    height: 110px;
    width: 100%;
    font-family: 'Anton', sans-serif;
    font-size: 146px;
    line-height: 110px;
    white-space: nowrap;
  }
  .title-row .initial {
    position: absolute;
    right: calc(100% - 190px);
    top: 0;
    color: var(--initial);
  }
  .title-row .rest {
    position: absolute;
    left: 228px;
    top: 0;
    letter-spacing: 2px;
  }
  .title-row--rise { top: 357px; }
  .title-row--shift { top: 491px; }
  .title-row--thrive { top: 625px; }
  .title-row--rise .rest,
  .title-row--thrive .rest { color: var(--brand-blue); }
  .title-row--shift .rest { color: var(--slate); }
  .closing-line {
    position: absolute;
    left: 232px;
    top: 790px;
    font-family: 'Josefin Sans', sans-serif;
    font-weight: 700;
    font-size: 21px;
    letter-spacing: 1px;
    color: var(--slate);
    white-space: nowrap;
  }
  .author {
    position: absolute;
    left: 232px;
    top: 918px;
    font-family: 'Anton', sans-serif;
    font-size: 48px;
    line-height: 1;
    letter-spacing: 2px;
    color: var(--slate);
  }
  .author .surname { color: var(--brand-blue); }
</style>
</head>
<body>
  <main class="book-cover">
    <div class="spine-band"></div>

    <div class="count">360</div>
    <p class="tagline tagline--one">BOLD <span class="accent">MOMENTUM</span> NOTES</p>
    <p class="tagline tagline--two">TO GUIDE ANYONE TO</p>

    <h1 aria-label="Rise. Shift. Thrive.">
      <span class="title-row title-row--rise"><span class="initial">R</span><span class="rest">ISE</span></span>
      <span class="title-row title-row--shift"><span class="initial">S</span><span class="rest">HIFT</span></span>
      <span class="title-row title-row--thrive"><span class="initial">T</span><span class="rest">HRIVE</span></span>
    </h1>

    <p class="closing-line">IN THEIR CAREER &amp; DAILY DREAMS.</p>

    <p class="author">KARIM <span class="surname">DELANO</span></p>
  </main>
</body>
</html>
```